Yard sign

I want it to look similar to this one,

change name to DRAVEK and submit new ideas

Also would like to improvise a bit. let's not make exactly the same thing

would like to change to: Connecticut #1 Company

also change phone to 203-555-0147
and website to
dravekllc.com

this is yard sign. size is 24' Width and 32' Height

Target Market(s)

Roof

Industry/Entity Type

Roofing

Requirements
Must have
• similar colors or add something new

```html
<!DOCTYPE html>
<html lang="en">
<head>
<meta charset="utf-8">
<title>Dravek Company Yard Sign</title>
<link rel="stylesheet" href="https://fonts.googleapis.com/css2?family=Anton&family=Montserrat:wght@700&display=swap">
<style>
  :root {
    --yellow: #fdd83d;
    --red: #ef2f19;
    --black: #161616;
    --white: #ffffff;
    --backdrop: #e3e3e3;
  }
  html, body {
    margin: 0;
    padding: 0;
    width: 1200px;
    height: 2872px;
    overflow: hidden;
    background: var(--backdrop);
  }
  .yard-sign {
    position: absolute;
    left: 75px;
    top: 734px;
    width: 1050px;
    height: 1403px;
    display: block;
  }
  .headline {
    font-family: "Anton", "Oswald", sans-serif;
  }
  .tagline { fill: var(--black); }
  .tagline-rank { fill: var(--red); }
  .brand-name {
    fill: var(--black);
    stroke: var(--white);
    stroke-width: 4;
    paint-order: stroke;
    stroke-linejoin: round;
  }
  .brand-suffix {
    fill: var(--red);
    stroke: var(--white);
    stroke-width: 4;
    paint-order: stroke;
    stroke-linejoin: round;
  }
  .phone-pill { fill: var(--yellow); }
  .phone-number { fill: var(--black); }
  .website {
    font-family: "Montserrat", "Arial", sans-serif;
    font-weight: 700;
    fill: var(--white);
  }
  .band-yellow { fill: var(--yellow); }
  .band-red { fill: var(--red); }
  .panel-black { fill: var(--black); }
</style>
</head>
<body>
<svg class="yard-sign" viewBox="0 0 610 815" role="img" aria-label="Dravek Company yard sign">
  <rect class="panel-black" x="0" y="0" width="610" height="815"/>
  <polygon class="band-yellow" points="0,0 610,0 610,155 0,200"/>
  <polygon class="band-red" points="0,220 610,170 610,375 0,430"/>
  <rect class="band-red" x="0" y="800" width="610" height="15"/>

  <text class="headline tagline" x="32" y="132" font-size="78" textLength="418" lengthAdjust="spacingAndGlyphs">CONNECTICUT</text>
  <text class="headline tagline-rank" x="464" y="132" font-size="104" textLength="116" lengthAdjust="spacingAndGlyphs">#1</text>

  <g transform="rotate(-5.5 305 374)">
    <text class="headline brand-name" x="35" y="374" font-size="190" textLength="545" lengthAdjust="spacingAndGlyphs">DRAVEK</text>
  </g>
  <g transform="rotate(-5.5 305 548)">
    <text class="headline brand-suffix" x="38" y="548" font-size="145" textLength="540" lengthAdjust="spacingAndGlyphs">COMPANY</text>
  </g>

  <rect class="phone-pill" x="52" y="603" width="505" height="95" rx="18"/>
  <text class="headline phone-number" x="305" y="679" font-size="78" text-anchor="middle" textLength="438" lengthAdjust="spacingAndGlyphs">203-555-0147</text>

  <text class="website" x="305" y="777" font-size="60" text-anchor="middle" textLength="410" lengthAdjust="spacingAndGlyphs">dravekllc.com</text>
</svg>
</body>
</html>
```